Grand Tart Drop Off

I am a Realtor and will be Mailing this Postcard to my best Clients Inviting them to Select the Pie they want for Thanksgiving and I will open my office for them to pick up. here's my thought on text:

THANK YOU GRAND TART DROP OFF!
Tues Nov 25th 3 to 8PM

In Giving Thanks for Your Support and Referrals I want to Personally Invite You to My 1st Annual "Grand Tart Dropoff". You have a choice of:
*Apple
*Pumpkin
*Pecan

Please let me know Your Choice by Mon Nov 17th. Please Feel Free to email me or Call Me with Your Pie Choice!

There will be Food and Drink Including My Award Winning Chili.

718 Birch Lane
Ardley Me 04127
dana@danavoreland.net
207.481.5967

Please Give it a Thanksgiving Look....I did not include a photo of a pie but open to it. PLEASE make the Paragraph "In Giving Thanks with the 3 Pie choices the Focal Point that Draws Your eyes to it.

```html
<!DOCTYPE html>
<html lang="en">
<head>
<meta charset="utf-8">
<title>Grand Tart Drop Off</title>
<link rel="stylesheet" href="https://fonts.googleapis.com/css2?family=Rye&family=Fredoka:wght@600&display=swap">
<style>
  :root {
    --paper: #ffffff;
    --card-grey: #ebebeb;
    --cocoa: #a5826f;
    --cocoa-text: #ecd0ad;
    --ribbon: #f15a29;
    --brown: #5e4126;
    --coral: #f37a58;
    --apple: #b3bb3a;
    --pumpkin: #f07b2e;
    --pecan: #4f3b28;
    --maroon: #8b1d1d;
    --pie-crust: #eea25e;
    --pie-tin: #c4c4c8;
    --fork-white: #fbfbfb;
  }
  * { box-sizing: border-box; margin: 0; padding: 0; }
  html, body { width: 1200px; height: 1031px; overflow: hidden; background: var(--paper); }
  .postcard {
    position: absolute; left: 23px; top: 6px; width: 1154px; height: 891px;
    background: var(--card-grey); overflow: hidden;
    font-family: "Rye", serif; font-variant-caps: small-caps;
  }
  .centered { position: absolute; left: 0; width: 100%; text-align: center; white-space: nowrap; }

  .header-band {
    position: absolute; left: 0; top: 0; width: 100%; height: 172px;
    background: var(--cocoa);
  }
  .event-title { top: 46px; font-size: 42px; line-height: 52px; color: var(--cocoa-text); letter-spacing: 1px; }
  .event-date { top: 101px; font-size: 24px; line-height: 30px; color: var(--cocoa-text); }

  .ribbon { position: absolute; left: 0; top: 148px; width: 1154px; height: 152px; }
  .ribbon-title {
    top: 162px; font-family: "Fredoka", sans-serif; font-weight: 600; font-variant-caps: normal;
    font-size: 100px; line-height: 120px; color: var(--paper); letter-spacing: 2px;
  }

  .invite { top: 308px; font-size: 29px; line-height: 35px; color: var(--brown); }
  .choice-heading {
    top: 378px; font-family: "Fredoka", sans-serif; font-weight: 600; font-variant-caps: normal;
    font-size: 62px; line-height: 72px; color: var(--coral);
  }

  .pie-art {
    position: absolute; top: 480px; width: 225px; height: 97px; border-radius: 10px;
    background: linear-gradient(180deg, var(--pie-crust) 0%, var(--pie-crust) 55%, var(--pie-tin) 56%, var(--pie-tin) 100%);
  }
  .pie-art.left { left: 123px; }
  .pie-art.right { left: 777px; }

  .pie-list { position: absolute; left: 445px; top: 440px; list-style: none; font-size: 36px; line-height: 49px; }
  .pie-list li { display: flex; align-items: center; gap: 12px; }
  .leaf { width: 36px; height: 36px; border-radius: 4px; display: inline-block; }
  .apple { color: var(--apple); } .apple .leaf { background: #9aa53a; }
  .pumpkin { color: var(--pumpkin); } .pumpkin .leaf { background: #d0712c; }
  .pecan { color: var(--pecan); } .pecan .leaf { background: #5b4430; }

  .cutlery-strip {
    position: absolute; left: 0; top: 680px; width: 100%; height: 211px;
    background: linear-gradient(180deg, #f6f6f6 0%, #fafafa 100%);
  }

  .extras { top: 597px; font-size: 22px; line-height: 28px; color: var(--brown); }
  .rsvp { top: 640px; font-size: 26px; line-height: 36px; color: var(--ribbon); }

  .contact {
    position: absolute; left: 450px; top: 738px; width: 300px; text-align: center;
    font-size: 22px; line-height: 31px; color: var(--brown); font-style: normal;
  }
  .brokerage {
    position: absolute; left: 752px; top: 780px; width: 315px; text-align: center;
    font-size: 34px; line-height: 44px; color: var(--maroon); white-space: nowrap;
  }
</style>
</head>
<body>
<main class="postcard">
  <div class="header-band" role="img" aria-label="Polka dot pattern band in warm browns"></div>
  <h1 class="centered event-title">THANK YOU GRAND TART DROP OFF!</h1>
  <p class="centered event-date">Tues Nov 25th 3-8 pm</p>

  <svg class="ribbon" viewBox="0 0 1154 152" aria-hidden="true">
    <rect x="0" y="23" width="1154" height="101" fill="var(--ribbon)"/>
    <polygon points="131,0 1023,0 1000,76 1023,152 131,152 154,76" fill="var(--paper)"/>
    <polygon points="140,6 1014,6 992,76 1014,146 140,146 162,76" fill="var(--ribbon)"/>
  </svg>
  <h2 class="centered ribbon-title">In Giving Thanks</h2>

  <p class="centered invite">For Your Support and Referrals I want to<br>Personally Invite You to My 1st Annual "Grand Tart Dropoff".</p>
  <h3 class="centered choice-heading">You have a choice of:</h3>

  <div class="pie-art left" role="img" aria-label="Illustration of a steaming baked pie"></div>
  <div class="pie-art right" role="img" aria-label="Illustration of a steaming baked pie"></div>

  <ul class="pie-list">
    <li class="apple"><span class="leaf" role="img" aria-label="Autumn leaf"></span>Apple</li>
    <li class="pumpkin"><span class="leaf" role="img" aria-label="Autumn leaf"></span>Pumpkin</li>
    <li class="pecan"><span class="leaf" role="img" aria-label="Autumn leaf"></span>Pecan</li>
  </ul>

  <div class="cutlery-strip" role="img" aria-label="Row of white fork silhouettes along the bottom edge"></div>

  <p class="centered extras">there will be food and drink including my award winning chili</p>
  <p class="centered rsvp">Please let me know Your Choice by Mon Nov 17th.<br>Please Feel Free to email me or Call Me with Your Pie Choice!</p>

  <address class="contact">
    718 Birch Lane<br>
    Ardley Me 04127<br>
    dana@danavoreland.net<br>
    207.481.5967
  </address>

  <div class="brokerage">Harborline Realty</div>
</main>
</body>
</html>
```